Board Game Inspired Referral Tracker

Hello,

I'm looking to have a graphic designed on approximately 4 x 6 card stock or magnet. The graphic is essentially to be a board game. This is a 1 sided card.

It's a referral tracking system (for real estate). For each referral given that results in a closing the client will receive an incentive to keep referring.

I see it as:

1st referral: upon closing you receive $100
2nd referral: upon closing you receive $250
3rd referral: upon closing you receive $250
4th referral: upon closing you receive $250
5th referral: upon closing you receive $1000

I'm open for creativity, however I'd like it to reflect my branding (brightmeadowlanestudio.com), include my logo but be very fun and somewhat interactive with cartoon-like inspiration (money bags/jackpot, bright colours, etc.). I'd like stickers to cover each referral box once it's been earned; they would have to be pre-cut / individual, these should be included in the design. I would like to see my logo incorporated in a creative way (see website for logo).

Ideally I'd like this to be ready to print by the end of this week, Friday, June 5th.

Looking forward to seeing your ideas!

Industry/Entity Type

Real Estate

Requirements
Must have
• My logo (Bright Meadow Lane Studio)
• My brokerage logo (Pellham Partners Realty) (small)
• "As a licensed Realtor®, my business thrives on trust and referrals from friends and family. I am pleased to offer you this generous incentive program for your support and enthusiasm.
• For each referral you send me that results in a successful closing, as a token of my gratitude, I will send you a gift certificate in the monetary amount indicated in the game below. Make it to five successful referrals and you’ll receive the jackpot!"
• Thank you for your support, and remember, I'm never too busy for your referrals.

```html
<!DOCTYPE html>
<html lang="en">
<head>
<meta charset="utf-8">
<title>Referral Rewards Game – Bright Meadow Lane Studio</title>
<link rel="stylesheet" href="https://fonts.googleapis.com/css2?family=Bebas+Neue&family=Cookie&family=Marcellus+SC&family=Open+Sans:ital,wght@0,400;0,700;0,800;1,300&display=block">
<style>
  :root {
    --teal-bg: #3b9b93;
    --teal-deep: #2f857d;
    --teal-shade: #2a7871;
    --teal-text: #2a9d95;
    --yellow: #e2df2b;
    --cream: #f2edc9;
    --white: #ffffff;
    --ink: #1d1d1d;
  }
  * { margin: 0; padding: 0; box-sizing: border-box; }
  html, body { width: 1200px; height: 900px; overflow: hidden; background: var(--white); }
  .card {
    position: relative; width: 1200px; height: 900px; overflow: hidden;
    background: var(--teal-bg);
    font-family: "Open Sans", Arial, sans-serif; color: var(--white);
  }
  .board { position: absolute; inset: 0; }

  .headline {
    position: absolute; left: 66px; top: 52px; width: 395px; overflow: hidden;
    white-space: nowrap;
    font-family: "Cookie", "Brush Script MT", cursive; font-weight: 400;
    font-size: 84px; line-height: 1; color: var(--white);
  }
  .jackpot-box {
    position: absolute; left: 66px; top: 138px; width: 364px; height: 276px;
    background: var(--yellow); text-align: center;
  }
  .jackpot-amount {
    font-family: "Bebas Neue", Impact, sans-serif; font-size: 84px; line-height: 1;
    color: var(--ink); margin-top: 28px;
  }
  .jackpot-cheer {
    font-weight: 700; font-size: 25px; color: var(--teal-text); margin-top: 14px; letter-spacing: 0.5px;
  }
  .jackpot-note {
    font-style: italic; font-weight: 300; font-size: 27px; line-height: 23px;
    color: var(--teal-text); margin-top: 8px;
  }

  .brokerage-name {
    position: absolute; left: 66px; top: 518px;
    font-size: 9.5px; letter-spacing: 2.6px; color: var(--ink); text-transform: uppercase;
  }
  .rules-title {
    position: absolute; left: 68px; top: 538px;
    font-family: "Bebas Neue", Impact, sans-serif; font-size: 42px; line-height: 1; color: var(--white);
  }
  .rules-list {
    position: absolute; left: 62px; top: 590px; width: 392px; list-style: none;
    font-size: 15.5px; line-height: 19px;
  }
  .rules-list li { position: relative; padding-left: 22px; margin-bottom: 10px; }
  .rules-list li::before {
    content: ""; position: absolute; left: 0; top: 6px; width: 8px; height: 8px;
    border-radius: 50%; background: var(--cream);
  }

  .jackpot-call {
    position: absolute; left: 500px; white-space: nowrap;
    font-family: "Bebas Neue", Impact, sans-serif;
    font-size: 28px; line-height: 1; word-spacing: 8px; letter-spacing: 0.3px; color: var(--white);
  }
  .jackpot-call.top { top: 78px; }
  .jackpot-call.bottom { top: 118px; }
  .star-number {
    position: absolute; left: 770px; top: 88px; width: 40px; text-align: center;
    font-family: "Bebas Neue", Impact, sans-serif; font-size: 54px; line-height: 1; color: var(--ink);
  }

  .studio-name {
    position: absolute; left: 490px; top: 252px; width: 600px; text-align: center;
    font-family: "Marcellus SC", Georgia, serif; font-size: 36px; color: var(--white); letter-spacing: 1px;
  }

  .step {
    position: absolute; font-family: "Bebas Neue", Impact, sans-serif; font-size: 62px;
    line-height: 1; color: var(--cream);
  }
  .step-1 { left: 774px; top: 640px; }
  .step-2 { left: 772px; top: 524px; }
  .step-3 { left: 673px; top: 372px; }
  .step-4 { left: 876px; top: 372px; }

  .reward {
    position: absolute; width: 132px; height: 97px; background: var(--white);
    text-align: center; color: var(--teal-text);
  }
  .reward-amount {
    font-family: "Bebas Neue", Impact, sans-serif; font-size: 46px; line-height: 1; margin-top: 8px;
  }
  .reward-text { font-size: 9.5px; font-weight: 700; line-height: 10px; }
  .reward-3 { left: 481px; top: 348px; }
  .reward-4 { left: 941px; top: 354px; }
  .reward-2 { left: 957px; top: 502px; }
  .reward-1 { left: 957px; top: 617px; }

  .start-badge {
    position: absolute; left: 666px; top: 748px; width: 244px; height: 62px;
    background: var(--cream); border: 3px solid var(--teal-deep); outline: 3px solid var(--cream);
    text-align: center; color: var(--teal-text);
  }
  .start-label {
    font-family: "Bebas Neue", Impact, sans-serif; font-size: 50px; line-height: 44px; letter-spacing: 1px;
  }
  .start-ribbon {
    position: absolute; left: 60px; bottom: -9px; width: 118px; height: 16px; background: var(--cream);
    border: 1.5px solid var(--teal-text); font-size: 8.5px; letter-spacing: 2px; line-height: 13px;
  }
</style>
</head>
<body>
<main class="card">
  <svg class="board" width="1200" height="900" viewBox="0 0 1200 900" aria-hidden="true">
    <g role="img" aria-label="Large isometric stacked-box backdrop in deep teal">
      <polygon points="785,140 1120,238 1120,722 785,862 450,722 450,238" fill="var(--teal-deep)"/>
      <polygon points="785,330 1000,400 1000,720 785,800 570,720 570,400" fill="var(--teal-shade)" opacity="0.45"/>
    </g>

    <rect x="470" y="103" width="260" height="5" fill="var(--yellow)"/>

    <g fill="var(--yellow)">
      <polygon points="790,68 801,98 833,98 807,117 817,148 790,129 763,148 773,117 747,98 779,98"/>
      <polygon points="750,58 755,70 768,70 758,78 762,91 750,83 738,91 742,78 732,70 745,70"/>
      <polygon points="822,58 827,70 840,70 830,78 834,91 822,83 810,91 814,78 804,70 817,70"/>
      <polygon points="737,120 742,132 755,132 745,140 749,153 737,145 725,153 729,140 719,132 732,132"/>
      <polygon points="838,120 843,132 856,132 846,140 850,153 838,145 826,153 830,140 820,132 833,132"/>
    </g>

    <g fill="none" stroke="var(--cream)" stroke-width="4" stroke-linecap="round" stroke-dasharray="0 10">
      <polyline points="826,104 893,104 893,230"/>
      <polyline points="893,312 893,370"/>
      <line x1="706" y1="400" x2="872" y2="400"/>
      <polyline points="640,400 660,400 655,525 712,585 770,552"/>
      <line x1="786" y1="578" x2="786" y2="640"/>
    </g>

    <g stroke="var(--cream)" stroke-width="4">
      <line x1="806" y1="550" x2="922" y2="550"/>
      <line x1="804" y1="665" x2="918" y2="665"/>
    </g>

    <g fill="none" stroke="var(--white)" stroke-width="4" stroke-linejoin="miter">
      <polyline points="618,382 638,400 618,418"/>
      <polyline points="937,384 917,402 937,420"/>
      <polyline points="953,532 933,550 953,568"/>
      <polyline points="953,647 933,665 953,683"/>
    </g>

    <polygon points="786,728 772,746 800,746" fill="var(--cream)"/>

    <circle cx="170" cy="470" r="35" fill="var(--yellow)"/>
  </svg>

  <h1 class="headline">Congratulations!</h1>
  <section class="jackpot-box">
    <p class="jackpot-amount">$1,000</p>
    <p class="jackpot-cheer">CONGRATULATIONS!</p>
    <p class="jackpot-note">This is your final reward<br>upon closing your<br>5th referral</p>
  </section>

  <p class="brokerage-name">Pellham Partners Realty</p>
  <h2 class="rules-title">Rules &amp; Regulations</h2>
  <ul class="rules-list">
    <li>As a licensed Realtor®, my business thrives on trust and referrals from friends and family. I am pleased to offer you this generous incentive program for your support and enthusiasm</li>
    <li>For each referral you send me that results in a successful closing, as a token of my gratitude, I will send you a gift certificate in the monetary amount indicated in the game below. Make it to five successful referrals and you’ll receive the jackpot</li>
    <li>Thank you for your support, and remember, I'm never too busy for your referrals!</li>
  </ul>

  <p class="jackpot-call top">JACKPOT! JACKPOT!</p>
  <p class="jackpot-call bottom">JACKPOT! JACKPOT!</p>
  <span class="star-number">5</span>

  <p class="studio-name">Bright Meadow Lane Studio</p>

  <span class="step step-1">1</span>
  <span class="step step-2">2</span>
  <span class="step step-3">3</span>
  <span class="step step-4">4</span>

  <div class="reward reward-3">
    <p class="reward-amount">$250</p>
    <p class="reward-text">Keep it up!<br>This is your reward upon<br>closing your 3rd referral</p>
  </div>
  <div class="reward reward-4">
    <p class="reward-amount">$250</p>
    <p class="reward-text">Almost there!<br>This is your reward upon<br>closing your 4th referral</p>
  </div>
  <div class="reward reward-2">
    <p class="reward-amount">$250</p>
    <p class="reward-text">Well done!<br>This is your reward upon<br>closing your 2nd referral</p>
  </div>
  <div class="reward reward-1">
    <p class="reward-amount">$100</p>
    <p class="reward-text">Good job!<br>This is your reward upon<br>closing your 1st referral</p>
  </div>

  <div class="start-badge">
    <p class="start-label">START HERE</p>
    <p class="start-ribbon">LIMITED × EDITION</p>
  </div>
</main>
</body>
</html>
```